Energy trading company (Voltrisa) needs a business card

We need a business card for a company based in Central America. Our main purpose is trading energy . We already have the logo but we need some good creativity to design a high impact business card. Colors blue, orange, green can be used or we would like to see good combinatios with our logo

Target Market(s)

Energy

Industry/Entity Type

Power Generation

Contact Information for Business Card

Logo , headquarters , name, background

Font styles to use
Serif
Sans Serif

Colors

Designer to choose colors to be used in the design.

Requirements
Must have
• it must have a fresh and clean view
Nice to have
• good backgrounds that combine with the logo
Should not have
• too much words

```html
<!DOCTYPE html>
<html lang="en">
<head>
<meta charset="utf-8">
<title>Voltrisa business card</title>
<link rel="stylesheet" href="https://fonts.googleapis.com/css2?family=Lato:wght@400;700&family=Arimo:wght@700&display=swap">
<style>
  :root {
    --backdrop: #2d2d2d;
    --card-white: #ffffff;
    --brand-orange: #f39323;
    --ink: #1e1e1e;
    --rule: #9a9a9a;
  }
  html, body {
    margin: 0;
    padding: 0;
    width: 1200px;
    height: 1200px;
    overflow: hidden;
    background: var(--backdrop);
  }
  .canvas {
    position: relative;
    width: 1200px;
    height: 1200px;
  }
  .card {
    position: absolute;
    top: 310px;
    width: 364px;
    height: 594px;
    box-shadow: 3px 4px 8px rgba(0,0,0,0.45);
  }
  .card-front {
    left: 234px;
    background: var(--card-white);
    font-family: "Lato", sans-serif;
    color: var(--ink);
    text-align: center;
  }
  .card-back {
    left: 627px;
    width: 369px;
    background: var(--brand-orange);
  }
  .brand {
    position: absolute;
    left: 0;
    right: 0;
    display: flex;
    flex-direction: column;
    align-items: center;
  }
  .brand-front {
    top: 108px;
  }
  .brand-dot {
    width: 74px;
    height: 74px;
    border-radius: 50%;
    background: var(--brand-orange);
    margin-bottom: 14px;
  }
  .brand-name {
    font-family: "Lato", sans-serif;
    font-weight: 400;
    font-size: 53px;
    line-height: 1;
    letter-spacing: 0.5px;
    color: var(--brand-orange);
  }
  .holder {
    position: absolute;
    top: 343px;
    left: 0;
    right: 0;
  }
  .holder-name {
    font-family: "Arimo", sans-serif;
    font-weight: 700;
    font-size: 21px;
    color: var(--brand-orange);
    line-height: 1;
  }
  .holder-role {
    font-size: 17px;
    margin-top: 2px;
  }
  .icon-row {
    position: absolute;
    top: 394px;
    left: 87px;
    width: 190px;
    height: 28px;
  }
  .contact {
    position: absolute;
    top: 430px;
    left: 0;
    right: 0;
    font-size: 17px;
    line-height: 22px;
  }
  .divider {
    position: absolute;
    top: 506px;
    left: 87px;
    width: 196px;
    height: 1px;
    background: #c4c4c4;
  }
  .address {
    position: absolute;
    top: 517px;
    left: 0;
    right: 0;
    font-size: 17px;
    line-height: 22px;
  }
  .brand-back {
    top: 210px;
  }
  .brand-back .brand-dot {
    width: 110px;
    height: 110px;
    background: var(--card-white);
    margin-bottom: 22px;
  }
  .brand-back .brand-name {
    color: var(--card-white);
    font-size: 58px;
  }
</style>
</head>
<body>
<main class="canvas">
  <section class="card card-front">
    <div class="brand brand-front">
      <div class="brand-dot"></div>
      <div class="brand-name">VOLTRISA</div>
    </div>

    <div class="holder">
      <div class="holder-name">MARCUS REYES</div>
      <div class="holder-role">Managing Director</div>
    </div>

    <svg class="icon-row" viewBox="0 0 190 28" aria-hidden="true">
      <line x1="0" y1="14" x2="52" y2="14" stroke="var(--rule)" stroke-width="1.5"/>
      <line x1="138" y1="14" x2="190" y2="14" stroke="var(--rule)" stroke-width="1.5"/>
      <circle cx="67" cy="14" r="12" fill="var(--brand-orange)"/>
      <path d="M61 11 q6 -5 12 0 l-2 2 h-8 z M62 13 h10 v6 h-10 z" fill="#fff"/>
      <circle cx="95" cy="14" r="12" fill="var(--brand-orange)"/>
      <rect x="88" y="9" width="14" height="10" fill="#fff"/>
      <path d="M88 9 l7 6 l7 -6" fill="none" stroke="var(--brand-orange)" stroke-width="1.2"/>
      <circle cx="123" cy="14" r="12" fill="var(--brand-orange)"/>
      <circle cx="123" cy="14" r="7" fill="#fff"/>
      <path d="M119 11 q3 1 3 4 q2 1 1 4 M126 9 q-1 3 2 4" fill="none" stroke="var(--brand-orange)" stroke-width="1.4"/>
    </svg>

    <div class="contact">
      052-870 314 226<br>
      hello@voltrisa.net<br>
      www.voltrisa.net
    </div>
    <div class="divider"></div>
    <div class="address">
      318, Calle Central Norte,<br>
      10104, Costa Rica
    </div>
  </section>

  <section class="card card-back">
    <div class="brand brand-back">
      <div class="brand-dot"></div>
      <div class="brand-name">VOLTRISA</div>
    </div>
  </section>
</main>
</body>
</html>
```